Website Design - BrightKeyHelpers.com

PLEASE CHECK WORD DOCUMENT ATTACHED FOR WEBSITE FLOW.

Target Market(s)

REAL ESTATE AGENTS ARE THE TARGET MARKET

Industry/Entity Type

Real Estate

Coding

Coded - Design and coding required

Number of Pages Required

4 page

Colors

Designer to choose colors to be used in the design.

Requirements
Must have
• WE LIKE RED LOGO ATTACHED
Nice to have
• PLEASE CHECK WORD DOCUMENT ATTACHED FOR WEBSITE FLOW.
Should not have

```html
<!DOCTYPE html>
<html lang="en">
<head>
<meta charset="utf-8">
<title>BrightKeyHelpers.com</title>
<link href="https://fonts.googleapis.com/css2?family=Lato:wght@400;700;900&family=Arimo:wght@400;700&display=swap" rel="stylesheet">
<style>
:root{
  --red:#e3001b;
  --red-dark:#c40017;
  --navy:#2b2a7d;
  --navy-deep:#25226f;
  --ink:#222;
  --muted:#555;
  --charcoal:#2d2d2d;
  --paper:#fff;
  --soft:#f4f4f4;
  --line:#d9d9d9;
}
*{margin:0;padding:0;box-sizing:border-box}
html,body{width:1200px;height:3774px;overflow:hidden}
body{font-family:"Lato",sans-serif;color:var(--ink);background:var(--paper);position:relative}
.abs{position:absolute}
.brand{font-family:"Lato",sans-serif;font-weight:900;color:var(--red);font-size:22px;line-height:1.1;display:flex;align-items:center;gap:10px}
.brand .mark{width:22px;height:22px;background:var(--red);display:inline-block}

/* header */
.topbar{left:0;top:0;width:1200px;height:118px;background:var(--paper)}
.topbar .brand{left:75px;top:40px}
.signup{left:566px;top:43px;display:flex;height:45px}
.signup .field{width:239px;border:1px solid var(--line);border-right:none;border-radius:23px 0 0 23px;font-size:13px;color:var(--muted);padding:13px 18px}
.signup .btn{width:101px;background:linear-gradient(90deg,var(--red),var(--navy));color:#fff;font-weight:700;font-size:14px;border-radius:0 23px 23px 0;display:flex;align-items:center;justify-content:center}
.callus{left:928px;top:42px;display:flex;align-items:center;gap:18px}
.callus .icon{width:42px;height:42px;border-radius:50%;background:var(--red);display:flex;align-items:center;justify-content:center}
.callus small{display:block;color:var(--red);font-weight:700;font-size:13px}
.callus strong{display:block;color:var(--red);font-weight:900;font-size:19px;margin-top:3px}

.mainnav{left:0;top:118px;width:1200px;height:58px;background:var(--navy)}
.mainnav span{position:absolute;top:21px;color:#fff;font-size:12px;font-weight:700}

/* hero */
.hero{left:0;top:176px;width:1200px;height:488px;background:linear-gradient(180deg,#6d7a8c 0%,#2f3566 35%,#2a2f55 60%,#3d5a2a 100%)}
.hero h1{position:absolute;left:130px;top:140px;width:940px;text-align:center;color:#fff;font-size:31px;font-weight:900;line-height:1.36}
.hero .arrow{position:absolute;top:172px}
.choices{top:601px;left:75px;display:flex;gap:30px}
.choice{width:330px;height:124px;border-radius:6px;background:linear-gradient(90deg,var(--red) 0%,var(--red) 35%,var(--navy) 100%);color:#fff;display:flex;flex-direction:column;align-items:center;justify-content:center;gap:14px;font-weight:700;font-size:13px;box-shadow:0 4px 10px rgba(0,0,0,.2)}

.section-title{position:absolute;left:0;width:1200px;text-align:center;font-weight:700;font-size:27px}

/* how it works */
.how .section-title{color:var(--navy)}
.step{position:absolute;width:240px;text-align:center}
.step .num{width:120px;height:120px;margin:0 auto;border-radius:50%;background:var(--navy-deep);color:#fff;font-size:38px;font-weight:700;display:flex;align-items:center;justify-content:center}
.step p{color:var(--navy);font-weight:700;font-size:24px;line-height:1.3;margin-top:18px}
.flow-arrow{position:absolute;top:910px}

/* packages */
.packages{left:0;top:1145px;width:1200px;height:601px;background:linear-gradient(180deg,#ececec 0%,#f6f6f6 30%,#fff 100%)}
.pkg{position:absolute;top:123px;width:202px;height:415px;background:#fff;border:1px solid var(--line);border-radius:8px;text-align:center;font-size:12.5px;line-height:1.65;color:#333}
.pkg .badge{width:90px;height:90px;border-radius:50%;background:var(--navy-deep);color:#fff;margin:18px auto 18px;display:flex;flex-direction:column;align-items:center;justify-content:center}
.pkg .badge small{font-size:12px}
.pkg .badge b{font-size:17px;font-weight:900}
.pkg p{padding:0 18px;margin-bottom:18px}
.pkg .buy{position:absolute;left:28px;bottom:30px;width:146px;height:40px;border-radius:20px;background:linear-gradient(90deg,var(--red),var(--navy));color:#fff;font-weight:700;font-size:13px;display:flex;align-items:center;justify-content:center}
.pkg.featured{background:linear-gradient(180deg,var(--red) 0%,var(--red-dark) 35%,var(--navy) 100%);color:#fff;border-color:transparent}
.pkg.featured .badge{background:#fff;color:var(--red);border:3px solid var(--red)}
.pkg.featured .buy{background:#fff;color:var(--red)}
.pkg .ribbon{position:absolute;left:-1px;top:87px;width:202px;height:17px;background:var(--red);color:#fff;font-size:10px;line-height:17px}

/* marketing services */
.perks{left:0;top:1746px;width:1200px;height:395px;background:var(--charcoal);color:#fff}
.perks h2{position:absolute;left:0;top:52px;width:1200px;text-align:center;font-size:28px;font-weight:900;line-height:1.35}
.perk{position:absolute;top:160px;width:250px;text-align:center}
.perk h3{font-size:21px;font-weight:700;margin:14px 0 8px}
.perk p{font-size:12.5px;line-height:1.6;color:#e6e6e6}

/* our services */
.svc{position:absolute;top:2257px;width:328px;height:234px;border:1px solid var(--line);background:#fafafa;box-shadow:0 2px 6px rgba(0,0,0,.12);text-align:center}
.svc svg{margin-top:24px}
.svc h3{font-size:20px;font-weight:700;margin:12px 0 10px}
.svc p{font-size:13px;line-height:1.7;color:var(--muted);padding:0 40px}

/* faq */
.faq-item{position:absolute;left:75px;width:1050px;border:1px solid var(--line);border-radius:4px;background:#fff;font-family:"Arimo",sans-serif}
.faq-item .q{height:62px;display:flex;align-items:center;justify-content:space-between;padding:0 28px;font-size:20px;color:#333}
.faq-item .a{background:#f0f0f0;padding:18px 22px;font-size:16px;line-height:1.6;color:#555;height:124px}

/* testimonial */
.testimonial{left:0;top:3125px;width:1200px;height:455px;background:var(--red)}
.testimonial h2{position:absolute;left:0;top:40px;width:1200px;text-align:center;color:#fff;font-size:28px;font-weight:700}
.quote-card{position:absolute;left:206px;top:108px;width:788px;height:284px;background:#fff;text-align:center;font-family:"Arimo",sans-serif}
.avatar{width:76px;height:76px;border-radius:50%;margin:55px auto 0;background:linear-gradient(160deg,#c9b8a8,#7b6f68)}
.quote-card p{font-size:15px;line-height:1.55;color:#444;padding:0 120px;margin-top:12px}
.quote-card h4{font-size:18px;font-weight:400;color:#333;margin-top:6px}
.quote-card small{font-size:12px;color:#555;display:block;margin-top:5px}
.dots{position:absolute;left:560px;top:416px;display:flex;gap:10px}
.dots i{width:10px;height:10px;border-radius:50%;background:#fff}

/* footer */
.footer{left:0;top:3580px;width:1200px;height:194px;background:var(--charcoal);color:#fff}
.footer .brand{position:absolute;left:75px;top:42px}
.footer .tag{position:absolute;left:95px;top:117px;width:280px;font-size:12px;font-weight:700;line-height:1.85}
.footnav span{position:absolute;top:50px;font-size:12.5px;font-weight:700}
.footer .copy{position:absolute;right:75px;top:82px;font-size:11px;color:#bbb}
.social{position:absolute;right:75px;top:120px;display:flex;gap:14px}
.social i{width:20px;height:20px;border-radius:50%;background:#fff;display:block}
</style>
</head>
<body>

<header class="abs topbar">
  <div class="abs brand"><span class="mark"></span>BrightKeyHelpers.com</div>
  <div class="abs signup"><div class="field">Enter Email Address</div><div class="btn">SIGN UP</div></div>
  <div class="abs callus">
    <div class="icon"><svg width="20" height="20" viewBox="0 0 24 24"><path fill="#fff" d="M6.6 10.8a15.1 15.1 0 0 0 6.6 6.6l2.2-2.2a1 1 0 0 1 1-.25 11.4 11.4 0 0 0 3.6.57 1 1 0 0 1 1 1V20a1 1 0 0 1-1 1A17 17 0 0 1 3 4a1 1 0 0 1 1-1h3.5a1 1 0 0 1 1 1c0 1.25.2 2.45.57 3.57a1 1 0 0 1-.25 1z"/></svg></div>
    <div><small>CALL OR TEXT US</small><strong>1-555-010-4477</strong></div>
  </div>
</header>

<nav class="abs mainnav">
  <span style="left:75px">HOW IT WORKS</span>
  <span style="left:219px">SERVICE AREA</span>
  <span style="left:352px">PRICING</span>
  <span style="left:445px">ABOUT US</span>
  <span style="left:551px">FAQ</span>
</nav>

<section class="abs hero" role="img" aria-label="Photo of a dark blue two-storey house with a green lawn and trees">
  <h1>Helping agents save time and money. We place signs and boost foot traffic to your&nbsp; open houses using proven marketing techniques.</h1>
  <svg class="arrow" style="left:62px" width="20" height="30" viewBox="0 0 20 30"><path d="M16 3 4 15l12 12" stroke="#fff" stroke-width="4" fill="none"/></svg>
  <svg class="arrow" style="left:1120px" width="20" height="30" viewBox="0 0 20 30"><path d="m4 3 12 12L4 27" stroke="#fff" stroke-width="4" fill="none"/></svg>
</section>

<div class="abs choices">
  <div class="choice">
    <svg width="26" height="28" viewBox="0 0 26 28"><circle cx="13" cy="8" r="7" fill="#fff"/><path d="M1 28c0-7 5-12 12-12s12 5 12 12z" fill="#fff"/></svg>
    I'M A FULL ON BROKERAGE
  </div>
  <div class="choice">
    <svg width="34" height="28" viewBox="0 0 34 28"><circle cx="17" cy="7" r="6" fill="#fff"/><circle cx="6" cy="10" r="4" fill="#fff"/><circle cx="28" cy="10" r="4" fill="#fff"/><path d="M7 26c0-6 4-11 10-11s10 5 10 11zM0 24c0-5 2-8 6-8 2 0 3 1 3 1-2 2-3 5-3 7zM34 24c0-5-2-8-6-8-2 0-3 1-3 1 2 2 3 5 3 7z" fill="#fff"/></svg>
    I'M AN IND. BROKER WITH A TEAM
  </div>
  <div class="choice">
    <svg width="28" height="28" viewBox="0 0 28 28"><rect x="2" y="4" width="22" height="22" rx="3" fill="none" stroke="#fff" stroke-width="3"/><path d="M10 18 22 4l4 3-12 14-5 1z" fill="#fff"/></svg>
    I NEED SIGN PLACEMENT ASAP
  </div>
</div>

<section class="how">
  <h2 class="section-title" style="top:790px">HOW IT WORKS</h2>
  <div class="step" style="left:119px;top:858px"><div class="num">01</div><p>CHOOSE<br>BROKERAGE/PRIVATE</p></div>
  <svg class="flow-arrow" style="left:362px" width="120" height="16" viewBox="0 0 120 16"><path d="M0 8h116M106 1l10 7-10 7" stroke="#8f8fc7" stroke-width="2" fill="none"/></svg>
  <div class="step" style="left:479px;top:858px"><div class="num">02</div><p>CHOOSE SIGNS</p></div>
  <svg class="flow-arrow" style="left:722px" width="120" height="16" viewBox="0 0 120 16"><path d="M0 8h116M106 1l10 7-10 7" stroke="#8f8fc7" stroke-width="2" fill="none"/></svg>
  <div class="step" style="left:839px;top:858px"><div class="num">02</div><p>PLACEMENT SIGNS</p></div>
</section>

<section class="abs packages">
  <h2 class="section-title" style="top:56px">PACKAGES</h2>
  <div class="pkg" style="left:75px"><div class="badge"><small>$49</small><b>5 SIGNS</b></div><p>Place signs strategically in best areas according to where the open house is located</p><p>Pick Up the signs after the open house</p><p>Store custom signs for you&nbsp; if needed</p><div class="buy">BUY NOW</div></div>
  <div class="pkg" style="left:288px"><div class="badge"><small>$59</small><b>10 SIGNS</b></div><p>Place signs strategically in best areas according to where the open house is located</p><p>Pick Up the signs after the open house</p><p>Store custom signs for you&nbsp; if needed</p><div class="buy">BUY NOW</div></div>
  <div class="pkg featured" style="left:501px"><div class="badge"><small>$69</small><b>15 SIGNS</b></div><p>Place signs strategically in best areas according to where the open house is located</p><p>Pick Up the signs after the open house</p><p>Store custom signs for you&nbsp; if needed</p><div class="buy">BUY NOW</div></div>
  <div class="pkg" style="left:712px"><div class="badge"><small>$79</small><b>20 SIGNS</b></div><p>Place signs strategically in best areas according to where the open house is located</p><p>Pick Up the signs after the open house</p><p>Store custom signs for you&nbsp; if needed</p><div class="buy">BUY NOW</div></div>
  <div class="pkg" style="left:923px"><div class="badge"><b>25+ SIGNS</b></div><div class="ribbon">Click Buy Now To Create Custom Pkg</div><p>Place signs strategically in best areas according to where the open house is located</p><p>Pick Up the signs after the open house</p><p>Store custom signs for you&nbsp; if needed</p><div class="buy">BUY NOW</div></div>
</section>

<section class="abs perks">
  <h2>SERVICES-SIGN UP FOR A SUBSCRIPTION AND GET<br>THESE MARKETING SERVICES FOR FREE</h2>
  <div class="perk" style="left:69px">
    <svg width="40" height="40" viewBox="0 0 40 40"><rect x="9" y="4" width="18" height="32" rx="3" fill="none" stroke="#fff" stroke-width="3"/><rect x="22" y="6" width="14" height="10" rx="2" fill="#fff"/></svg>
    <h3>SMS</h3><p>Send sms blast to your neighborhood informing them your home is for sale and if they know anyone looking to send them over</p>
  </div>
  <div class="perk" style="left:338px">
    <svg width="48" height="40" viewBox="0 0 48 40"><rect x="2" y="4" width="44" height="32" rx="2" fill="#fff"/><path d="M2 6l22 17L46 6" stroke="var(--charcoal)" stroke-width="3" fill="none"/></svg>
    <h3>EMAIL</h3><p>Send email blast to your neighborhood informing them your home is for sale and if they know anyone looking to send them over</p>
  </div>
  <div class="perk" style="left:607px">
    <svg width="40" height="40" viewBox="0 0 40 40"><rect x="2" y="2" width="36" height="36" rx="6" fill="#fff"/></svg>
    <h3>FB AD</h3><p>Newsfeed ads to people in your open house area</p>
  </div>
  <div class="perk" style="left:876px">
    <svg width="44" height="40" viewBox="0 0 44 40"><path d="M22 3 2 21h6v16h10V26h8v11h10V21h6z" fill="#fff"/></svg>
    <h3>VB</h3><p>Send VB blast to your neighborhood informing them your home is for sale and if they know anyone looking to send them over</p>
  </div>
</section>

<section class="our-services">
  <h2 class="section-title" style="top:2187px">OUR SERVICES</h2>
  <div class="svc" style="left:63px">
    <svg width="80" height="80" viewBox="0 0 80 80"><rect x="6" y="14" width="56" height="32" fill="none" stroke="var(--red)" stroke-width="3"/><path d="M6 8h60M64 4v74M14 20h40" stroke="var(--red)" stroke-width="3"/></svg>
    <h3>Lorium ipsum</h3><p>Eu in ultricies ut molestie viverra quisque leo vitae pede vitae curabitur.</p>
  </div>
  <div class="svc" style="left:436px">
    <svg width="80" height="80" viewBox="0 0 80 80"><path d="M8 70V50h10v20M24 70V40h10v30M40 70V30h10v30" fill="none" stroke="var(--red)" stroke-width="3"/><path d="M8 38 30 18l10 8 20-18" stroke="var(--red)" stroke-width="3" fill="none"/><circle cx="62" cy="60" r="13" fill="none" stroke="var(--red)" stroke-width="3"/><path d="M62 52v16M58 56h7M58 63h7" stroke="var(--red)" stroke-width="2"/></svg>
    <h3>Dolar Amit</h3><p>Eu in ultricies ut molestie viverra quisque leo vitae pede vitae curabitur.</p>
  </div>
  <div class="svc" style="left:810px">
    <svg width="80" height="80" viewBox="0 0 80 80"><circle cx="24" cy="18" r="12" fill="none" stroke="var(--red)" stroke-width="3"/><path d="M24 11v14M20 14h7M20 22h7" stroke="var(--red)" stroke-width="2"/><circle cx="46" cy="38" r="10" fill="none" stroke="var(--navy)" stroke-width="3"/><path d="M26 74c0-12 9-20 20-20s20 8 20 20z" fill="none" stroke="var(--red)" stroke-width="3"/></svg>
    <h3>Nemo enim</h3><p>Eu in ultricies ut molestie viverra quisque leo vitae pede vitae curabitur.</p>
  </div>
</section>

<section class="faq">
  <h2 class="section-title" style="top:2567px">FAQ</h2>
  <div class="faq-item" style="top:2652px">
    <div class="q">LOREM IPSUM IS SIMPLY DUMMY TEXT OF THE PRINTING?<svg width="18" height="12" viewBox="0 0 18 12"><path d="m2 2 7 7 7-7" stroke="#333" stroke-width="3" fill="none"/></svg></div>
    <div class="a">Lorem ipsum dolor sit amet, consectetur adipiscing elit, sed do eiusmod tempor incididunt ut labore et dolore magna aliqua. Ut enim ad minim veniam, quis nostrud exercitation ullamco laboris nisi ut aliquip ex ea commodo consequat. Duis aute irure dolor in reprehenderit in voluptate velit esse cillum dolore eu fugiat nulla pariatur.</div>
  </div>
  <div class="faq-item" style="top:2848px"><div class="q">LOREM IPSUM IS SIMPLY DUMMY TEXT OF THE PRINTING?<svg width="12" height="18" viewBox="0 0 12 18"><path d="m2 2 7 7-7 7" stroke="#333" stroke-width="3" fill="none"/></svg></div></div>
  <div class="faq-item" style="top:2924px"><div class="q">LOREM IPSUM IS SIMPLY DUMMY TEXT OF THE PRINTING?<svg width="12" height="18" viewBox="0 0 12 18"><path d="m2 2 7 7-7 7" stroke="#333" stroke-width="3" fill="none"/></svg></div></div>
  <div class="faq-item" style="top:2999px"><div class="q">LOREM IPSUM IS SIMPLY DUMMY TEXT OF THE PRINTING?<svg width="12" height="18" viewBox="0 0 12 18"><path d="m2 2 7 7-7 7" stroke="#333" stroke-width="3" fill="none"/></svg></div></div>
</section>

<section class="abs testimonial">
  <h2>TESTIMONIAL</h2>
  <div class="quote-card">
    <div class="avatar" role="img" aria-label="Portrait photo of the client"></div>
    <p>"Suspendisse et quis. Ante est feugiat. Urna odio tristique. Amet vel semper. Turpis hac in mattis quam placerat tincidunt magna aliquet"</p>
    <h4>Lena</h4>
    <small>Freelancer, Belgium</small>
  </div>
  <div class="dots"><i></i><i></i><i></i><i></i></div>
</section>

<footer class="abs footer">
  <div class="brand"><span class="mark"></span>BrightKeyHelpers.com</div>
  <p class="tag">Helping agents leverage their time and skills to increase production at an affordable price with impeccable support.</p>
  <div class="footnav">
    <span style="left:624px">HOW IT WORKS</span>
    <span style="left:767px">SERVICE AREA</span>
    <span style="left:898px">PRICING</span>
    <span style="left:992px">ABOUT US</span>
    <span style="left:1098px">FAQ</span>
  </div>
  <div class="copy">Copyright © 2018, Company Name. All Right Reserved</div>
  <div class="social"><i></i><i></i><i></i><i></i><i></i></div>
</footer>

</body>
</html>
```